Industry: Christian Ministry using Magic, Music and Multimedia to teach gospel

“Lanternfold Ministries brings the Gospel of Jesus Christ, with heart-seeking, biblical accuracy
through live, entertainment-based evangelistic Celebrations."

We are a service that wants to partner with christian religious institutions and churches to teach biblical gospel in a fun and entertaining way using magic.

Design inspiration: https://www.quillmarshwonders.example

DO NOT CONTACT ME PRIVATELY. IT WILL BE IGNORED.

Important:
1. Use only royalty free graphics
2. Use only google fonts
3. A clean, linear layout
4. Do not include search

PAGES

1. Home
2. Shows & Skylark
3. About Lanternfold
4. Media
5. Contact & Support

Color pallets
#0053E0
#FF2500
#ffffff

Please see attachment for more detail

Target Market(s)

Churches and christian schools

Industry/Entity Type

magic, entertainment, christianity

Number of Pages Required

5+ page

Colors
0054AA
0677BA
7BADD7
CADEEF
E8F1F8

Requirements
Should not have
• - search bar

```html
<!DOCTYPE html>
<html lang="en">
<head>
<meta charset="utf-8">
<title>Lanternfold Ministries</title>
<link href="https://fonts.googleapis.com/css2?family=Roboto:wght@400;500;700&display=swap" rel="stylesheet">
<style>
:root{
  --navy:#031640;
  --red:#ff2500;
  --fund-band:#b01a00;
  --fund-dark:#7e1000;
  --white:#ffffff;
  --ink:#1b1b1b;
  --muted:#f5f5f5;
  --line:#dddddd;
  --blue:#0053e0;
}
*{margin:0;padding:0;box-sizing:border-box}
html,body{width:1200px;height:3672px;overflow:hidden}
body{font-family:"Roboto",Arial,sans-serif;color:var(--ink);background:var(--white);position:relative}
.abs{position:absolute}
.photo{position:absolute}
.btn-red{position:absolute;background:var(--red);color:var(--white);font-size:18px;font-weight:500;display:flex;align-items:center;justify-content:center}
p.body{font-size:11.5px;line-height:22.5px;color:#222}

/* hero */
.hero{position:absolute;left:0;top:0;width:1200px;height:646px;background:linear-gradient(180deg,#4a3526 0%,#7a5638 40%,#9a4a32 75%,#5e3a2a 100%)}
.hero .shade{position:absolute;inset:0;background:rgba(0,0,0,.25)}
.brand{position:absolute;left:113px;top:36px;font-size:19px;font-weight:700;color:var(--white)}
.nav{position:absolute;right:112px;top:38px;display:flex;gap:22px;font-size:15px;font-weight:500;color:var(--white)}
.hero h1{position:absolute;left:0;width:1200px;top:232px;text-align:center;color:var(--white);font-size:44px;font-weight:700;line-height:56px}
.hero .lead{position:absolute;left:280px;width:640px;top:366px;text-align:center;color:var(--white);font-size:14.5px;line-height:22px}
.hero .explore{position:absolute;left:518px;top:434px;width:164px;height:47px;background:var(--white);color:var(--ink);font-size:18px;font-weight:500;display:flex;align-items:center;justify-content:center}

/* about */
.about h2{position:absolute;left:716px;top:694px;font-size:30px;font-weight:500}
.about .text{position:absolute;left:716px;top:746px;width:360px}

/* services */
.services{position:absolute;left:0;top:1229px;width:1200px;height:474px;background:var(--navy);color:var(--white)}
.service{position:absolute;width:240px}
.service svg{display:block}
.service h3{font-size:15px;font-weight:500;margin-top:10px}
.service p{font-size:10.5px;line-height:19px;margin-top:12px;color:#e6e9f0}
.service .more{font-size:10px;font-weight:700;margin-top:12px}
.services h2{position:absolute;right:112px;top:34px;width:420px;text-align:right;font-size:30px;font-weight:700;line-height:45px}

/* shows */
.shows-circle{position:absolute;left:138px;top:1748px;width:441px;height:441px;border-radius:50%;background:linear-gradient(135deg,#f4edc4 0%,#8a6a4a 45%,#3a2a3a 100%)}
.shows-badge{position:absolute;left:245px;top:1855px;width:228px;height:228px;border-radius:50%;background:var(--white);display:flex;align-items:center;justify-content:center;text-align:center;font-size:22px;font-weight:500;line-height:30px}
.shows h2{position:absolute;left:668px;top:1790px;font-size:30px;font-weight:500}
.shows .text{position:absolute;left:670px;top:1853px;width:400px}

/* events */
.events{position:absolute;left:0;top:2228px;width:1200px;height:548px;background:var(--muted)}
.events h2{position:absolute;left:0;width:1200px;top:30px;text-align:center;font-size:30px;font-weight:500}
.card{position:absolute;top:88px;width:309px;height:418px;background:var(--white);border:1px solid var(--line)}
.card .img{height:213px}
.card h3{position:absolute;left:31px;top:232px;font-size:18px;font-weight:500;line-height:22px;width:240px}
.card .meta{position:absolute;left:31px;font-size:11px;display:flex;align-items:center;gap:10px}
.count{position:absolute;left:31px;top:356px;display:flex;gap:6px}
.count .unit{width:40px;text-align:center}
.count .num{width:40px;height:40px;border-radius:50%;background:var(--white);box-shadow:0 1px 5px rgba(0,0,0,.18);font-size:12px;font-weight:500;display:flex;align-items:center;justify-content:center}
.count .lab{font-size:7.5px;color:#555;margin-top:5px}

/* follow */
.follow h2{position:absolute;left:751px;top:2836px;font-size:38px;font-weight:700;line-height:45px}
.follow .sub{position:absolute;left:752px;top:2948px;font-size:15px}
.social{position:absolute;display:flex}
.social span{background:var(--navy);color:var(--white);font-weight:700;display:flex;align-items:center;justify-content:center}

/* fund */
.fund{position:absolute;left:114px;top:3316px;width:974px;height:142px;background:var(--fund-band);color:var(--white)}
.fund .side{position:absolute;top:0;width:210px;height:142px;background:var(--fund-dark)}
.fund .side .amt{height:92px;display:flex;align-items:center;justify-content:center;font-size:30px;border-bottom:1px solid rgba(255,255,255,.35)}
.fund .side .lab{height:50px;display:flex;align-items:center;justify-content:center;font-size:15px}
.fund h2{position:absolute;left:248px;top:50px;font-size:29px;font-weight:700}
.fund .donate{position:absolute;left:556px;top:48px;width:164px;height:46px;background:var(--white);color:var(--ink);font-size:14px;font-weight:500;display:flex;align-items:center;justify-content:center}

/* footer */
.footer{position:absolute;left:0;top:3502px;width:1200px;height:170px;background:var(--navy);color:var(--white)}
.footer .name{position:absolute;left:113px;top:36px;font-size:18px;font-weight:700}
.footer ul{position:absolute;list-style:none;font-size:11px;line-height:19px}
.footer .copy{position:absolute;left:113px;top:138px;font-size:9.5px}
.footer .news{position:absolute;left:791px;top:34px;font-size:21px;font-weight:500}
.footer .field{position:absolute;left:791px;top:75px;width:201px;height:30px;background:var(--white);color:#555;font-size:9.5px;padding-left:14px;display:flex;align-items:center;border:1px solid #ccc}
.footer .sub-btn{position:absolute;left:992px;top:75px;width:96px;height:30px;background:var(--white);color:var(--ink);font-size:11px;font-weight:700;display:flex;align-items:center;justify-content:center;border:1px solid #ccc}
</style>
</head>
<body>

<!-- Hero -->
<header class="hero" role="img" aria-label="Church nave with stone arches and checkered floor">
  <div class="shade"></div>
  <div class="brand">Lanternfold Ministries</div>
  <nav class="nav"><span>Home</span><span>Shows &amp; Skylark</span><span>About Lanternfold</span><span>Media</span><span>Contact &amp; Support</span></nav>
  <h1>Love God.Love people.<br>Make disciples of Jesus Christ.</h1>
  <p class="lead">Our common creed is our belief in the Bible, our deep faith in Jesus Christ, and our acceptance of the unconditional love of God.</p>
  <div class="explore">Explore Now</div>
</header>

<!-- About -->
<section class="about">
  <div class="photo" style="left:114px;top:713px;width:292px;height:420px;background:linear-gradient(160deg,#e8e0cf,#b9a98a 60%,#6f7a5e)" role="img" aria-label="Bell arch with a woman reading beside it"></div>
  <div class="photo" style="left:427px;top:690px;width:243px;height:237px;background:linear-gradient(180deg,#b9c9d6 0%,#8fa3b3 45%,#8a3a26 75%,#6a2a1c)" role="img" aria-label="Red brick chapel tower with a cross"></div>
  <div class="photo" style="left:427px;top:946px;width:243px;height:237px;background:linear-gradient(150deg,#1e2a44 0%,#3a3f52 50%,#c9b89a 100%)" role="img" aria-label="Hands with rosary over an open bible"></div>
  <h2>About Lanternfold</h2>
  <div class="text">
    <p class="body">The gospel is the good news of God’s grace invading the darkness of this world. It is the grand narrative of creation, fall, redemption, and consummation ordained by God and orchestrated through the life, death, resurrection, and ascension of Jesus Christ. Christ’s crucifixion is the heart of the gospel. His resurrection is the power of the gospel. His ascension is the glory of the gospel.</p>
    <p class="body" style="margin-top:22px"><b style="font-weight:500">Christ’s death is a substitutionary and propitiatory sacrifice to God for our sins.</b><br>It satisfies the demands of God’s holy justice and appeases His holy wrath. It also demonstrates His mysterious love and reveals His amazing grace. Jesus Christ is the only mediator between God and man. There is no other name by which men can be saved.<br>At the heart of all sound doctrine is the cross of Jesus Christ and the infinite privilege that redeemed sinners have in glorifying God because of what He has accomplished.</p>
  </div>
  <div class="btn-red" style="left:716px;top:1136px;width:164px;height:47px">Learn More</div>
</section>

<!-- Services -->
<section class="services">
  <div class="service" style="left:113px;top:52px">
    <svg width="44" height="42" viewBox="0 0 44 42" fill="none" stroke="#ff2500" stroke-width="2"><path d="M6 30 L18 12 L24 16 L30 6 M14 36 L26 20 L34 24 L40 12"/><path d="M4 38 L14 30"/></svg>
    <h3>Praise &amp; Worship</h3>
    <p>Our church is open and friendly with many social activities. To keep our church running smoothly, we have committees .</p>
    <div class="more">Read More &nbsp;›</div>
  </div>
  <div class="service" style="left:411px;top:52px">
    <svg width="44" height="42" viewBox="0 0 44 42" fill="none" stroke="#ff2500" stroke-width="2"><circle cx="22" cy="15" r="10"/><path d="M6 40 C8 28 36 28 38 40 Z"/></svg>
    <h3>Counseling</h3>
    <p>We exist to represent Christ to our community and world so that they might see Jesus and realize all that God has planned for them!</p>
    <div class="more">Read More &nbsp;›</div>
  </div>
  <div class="service" style="left:113px;top:252px">
    <svg width="44" height="42" viewBox="0 0 44 42" fill="none" stroke="#ff2500" stroke-width="2"><path d="M4 8 L22 12 L40 8 L40 38 L22 40 L4 38 Z"/><path d="M22 12 V40"/></svg>
    <h3>Exhortation</h3>
    <p>We invite you to see for yourself how exciting church can be when the focus is simple and people are free to go after God with passion.</p>
    <div class="more">Read More &nbsp;›</div>
  </div>
  <div class="service" style="left:411px;top:252px">
    <svg width="44" height="42" viewBox="0 0 44 42" fill="none" stroke="#ff2500" stroke-width="2"><path d="M22 2 V10 M18 6 H26"/><path d="M6 22 L22 10 L38 22"/><path d="M8 20 V40 H36 V20"/><path d="M18 40 V30 H26 V40"/></svg>
    <h3>Harborlight Hosted Here</h3>
    <p>Join our weekly live-stream and online midweek programming to experience Harborlight from anywhere.</p>
    <div class="more">Read More &nbsp;›</div>
  </div>
  <h2>Keeping our church running smoothly</h2>
  <div class="photo" style="left:698px;top:125px;width:414px;height:335px;background:radial-gradient(circle at 50% 48%,#c7ccd8 0%,#4a5576 25%,rgba(3,22,64,0) 62%)" role="img" aria-label="Painted white cross with splatter texture"></div>
</section>

<!-- Shows -->
<section class="shows">
  <div class="shows-circle" role="img" aria-label="Teacher and child reading scripture in church pews"></div>
  <div class="shows-badge">Lanternfold<br>Ministries</div>
  <svg class="abs" style="left:267px;top:1877px" width="184" height="184" viewBox="0 0 184 184" fill="none">
    <circle cx="92" cy="92" r="86" stroke="#555" stroke-width="1" stroke-dasharray="2 3"/>
    <circle cx="92" cy="6" r="4.5" fill="#0053e0"/><circle cx="92" cy="178" r="4.5" fill="#031640"/>
    <circle cx="6" cy="92" r="4.5" fill="#ff2500"/><circle cx="178" cy="92" r="4.5" fill="#ff2500"/>
  </svg>
  <h2>Shows &amp; Skylark</h2>
  <div class="text">
    <p class="body">At Harborlight, we refer to the discipleship journey as the Transformational Loop – becoming more like Jesus as we grow in faith. We want to help you Follow Jesus with your life, Grow Together in community, Serve One Another with your unique gifts, and Change the World with the love of Christ. If you’re ready to take your next step of faith, we are here to help.</p>
    <p class="body" style="margin-top:22px">Overwhelmed by the gift of salvation we have found in Jesus, we have a heart for authentic worship, are passionate about the local church, and are on mis-sion to see God’s kingdom established across the earth.</p>
  </div>
  <div class="btn-red" style="left:671px;top:2091px;width:164px;height:47px">Learn More</div>
</section>

<!-- Events -->
<section class="events">
  <h2>Upcoming Events</h2>
  <article class="card" style="left:114px">
    <div class="img" style="background:linear-gradient(160deg,#6a4a36,#3a2a22 60%,#8a6a50)" role="img" aria-label="Two men talking in church pews"></div>
    <h3>Kingdom Roots in the Classroom</h3>
    <div class="meta" style="top:299px"><svg width="10" height="13" viewBox="0 0 10 13"><path d="M5 0 A5 5 0 0 1 10 5 C10 8 5 13 5 13 C5 13 0 8 0 5 A5 5 0 0 1 5 0Z" fill="#222"/><circle cx="5" cy="5" r="2" fill="#fff"/></svg>10 01, 2024</div>
    <div class="meta" style="top:321px"><svg width="12" height="12" viewBox="0 0 12 12"><rect x="0.5" y="1.5" width="11" height="10" fill="none" stroke="#222"/><rect x="0.5" y="1.5" width="11" height="3" fill="#222"/></svg>Harrowmere, UK</div>
    <div class="count"><div class="unit"><div class="num">266</div><div class="lab">Days</div></div><div class="unit"><div class="num">28</div><div class="lab">Hours</div></div><div class="unit"><div class="num">50</div><div class="lab">Minutes</div></div><div class="unit"><div class="num">67</div><div class="lab">Seconds</div></div></div>
  </article>
  <article class="card" style="left:446px">
    <div class="img" style="background:linear-gradient(160deg,#e6e6e6,#b5b5b5 50%,#5a4a40)" role="img" aria-label="Hands holding a rosary with a cross"></div>
    <h3>Youth Worship Services</h3>
    <div class="meta" style="top:299px"><svg width="10" height="13" viewBox="0 0 10 13"><path d="M5 0 A5 5 0 0 1 10 5 C10 8 5 13 5 13 C5 13 0 8 0 5 A5 5 0 0 1 5 0Z" fill="#222"/><circle cx="5" cy="5" r="2" fill="#fff"/></svg>10 01, 2024</div>
    <div class="meta" style="top:321px"><svg width="12" height="12" viewBox="0 0 12 12"><rect x="0.5" y="1.5" width="11" height="10" fill="none" stroke="#222"/><rect x="0.5" y="1.5" width="11" height="3" fill="#222"/></svg>Harrowmere, UK</div>
    <div class="count"><div class="unit"><div class="num">266</div><div class="lab">Days</div></div><div class="unit"><div class="num">28</div><div class="lab">Hours</div></div><div class="unit"><div class="num">50</div><div class="lab">Minutes</div></div><div class="unit"><div class="num">67</div><div class="lab">Seconds</div></div></div>
  </article>
  <article class="card" style="left:777px">
    <div class="img" style="background:linear-gradient(160deg,#7a5a42,#c9b29a 50%,#e9e2d8)" role="img" aria-label="Woman and two girls reading together at a table"></div>
    <h3>Youth is Gathering To Learn Music</h3>
    <div class="meta" style="top:299px"><svg width="10" height="13" viewBox="0 0 10 13"><path d="M5 0 A5 5 0 0 1 10 5 C10 8 5 13 5 13 C5 13 0 8 0 5 A5 5 0 0 1 5 0Z" fill="#222"/><circle cx="5" cy="5" r="2" fill="#fff"/></svg>10 01, 2024</div>
    <div class="meta" style="top:321px"><svg width="12" height="12" viewBox="0 0 12 12"><rect x="0.5" y="1.5" width="11" height="10" fill="none" stroke="#222"/><rect x="0.5" y="1.5" width="11" height="3" fill="#222"/></svg>Harrowmere, UK</div>
    <div class="count"><div class="unit"><div class="num">266</div><div class="lab">Days</div></div><div class="unit"><div class="num">28</div><div class="lab">Hours</div></div><div class="unit"><div class="num">50</div><div class="lab">Minutes</div></div><div class="unit"><div class="num">67</div><div class="lab">Seconds</div></div></div>
  </article>
</section>

<!-- Follow -->
<section class="follow">
  <div class="photo" style="left:154px;top:2817px;width:137px;height:128px;background:radial-gradient(circle at 50% 40%,#c0703a,#3a2418 70%)" role="img" aria-label="Glowing cross over an open book"></div>
  <div class="photo" style="left:123px;top:2968px;width:168px;height:160px;background:linear-gradient(160deg,#3a4a2a,#6a7a5a 50%,#2a3a2a)" role="img" aria-label="Preacher speaking outdoors, video"></div>
  <svg class="abs" style="left:195px;top:3036px" width="24" height="24" viewBox="0 0 24 24"><path d="M4 2 L22 12 L4 22 Z" fill="#fff"/></svg>
  <div class="photo" style="left:154px;top:3145px;width:137px;height:128px;background:radial-gradient(circle at 50% 30%,#f4e6c0,#8a6a4a 45%,#2a1e18)" role="img" aria-label="Person with raised arms before a bright cross"></div>
  <div class="photo" style="left:315px;top:2917px;width:342px;height:356px;background:linear-gradient(150deg,#6a5a4a,#2a2220 45%,#1a1614 80%)" role="img" aria-label="Woman praying with hands clasped over a bible"></div>
  <div class="photo" style="left:683px;top:3145px;width:137px;height:128px;background:linear-gradient(150deg,#5a4a3a,#c8b49a 60%,#7a6a5a)" role="img" aria-label="Family reading the bible together, video"></div>
  <svg class="abs" style="left:740px;top:3197px" width="24" height="24" viewBox="0 0 24 24"><path d="M4 2 L22 12 L4 22 Z" fill="#fff"/></svg>
  <div class="photo" style="left:861px;top:3086px;width:137px;height:129px;background:linear-gradient(150deg,#2a2420,#6a5446 50%,#b8a48e)" role="img" aria-label="Hands holding a closed bible"></div>
  <h2>Follow Us<br>@Lanternfold Ministries</h2>
  <div class="sub">Join the adventure, be part of our stories!</div>
  <div class="social" style="left:752px;top:2998px;gap:14px">
    <span style="width:36px;height:36px;font-size:12px">FB</span><span style="width:36px;height:36px;font-size:12px">IG</span><span style="width:36px;height:36px;font-size:12px">TW</span><span style="width:36px;height:36px;font-size:12px">YT</span>
  </div>
</section>

<!-- Fund -->
<section class="fund">
  <div class="side" style="left:0"><div class="amt">$7000</div><div class="lab">Needed Donation</div></div>
  <h2>Help Us Raise Funds</h2>
  <div class="donate">Donate Now</div>
  <div class="side" style="right:0"><div class="amt">$5060</div><div class="lab">Needed Donation</div></div>
</section>

<!-- Footer -->
<footer class="footer">
  <div class="name">Lanternfold Ministries</div>
  <div class="social" style="left:113px;top:86px;gap:13px">
    <span style="width:28px;height:28px;font-size:9px;border:1px solid rgba(255,255,255,.4)">FB</span><span style="width:28px;height:28px;font-size:9px;border:1px solid rgba(255,255,255,.4)">IG</span><span style="width:28px;height:28px;font-size:9px;border:1px solid rgba(255,255,255,.4)">TW</span><span style="width:28px;height:28px;font-size:9px;border:1px solid rgba(255,255,255,.4)">YT</span>
  </div>
  <div class="copy">©2023 Lanternfoldministries</div>
  <ul style="left:314px;top:33px"><li>Price and Workshop</li><li>Our Ministries</li><li>Our Pastors</li><li>Sermons &amp; Exhortations</li><li>Charity &amp; Volunteering</li></ul>
  <ul style="left:483px;top:33px"><li>Home</li><li>Shows &amp; Skylark</li><li>About Lanternfold</li><li>Media</li><li>Contact &amp; Support</li></ul>
  <ul style="left:627px;top:33px"><li>Telephone :</li><li>(123) 555 0148</li><li>Email :</li><li>hello@lanternfold.example</li><li>Address :</li><li>House # 27 Fenwick Row</li></ul>
  <div class="news">Subscribe To Our Newslatter</div>
  <div class="field">Enter your email</div>
  <div class="sub-btn">Subscribe</div>
</footer>

</body>
</html>
```